Corvo Halden is a Smart Device and Wiring Business offering the latest in Smart Home Devices inc

Looking for a new website to draw people to my business and explain what a smart home is all about. I currently own a domain and have a website I put together in godaddy business website builder. address www.corvohalden.com. The website needs modernising and be visually appealing with cool action buttons, client feedback page etc.

The webpage needs to present an image of seamless integration of wireless voice control and smart devices that take tasks and activities away from the owner saving them time and money.

I have a chatterloop business page(corvo halden) and snapquill linked with the business, are we able to link this to the website somehow?

Target Market(s)

Residential home owners who want to modernise their home. Who have seen adverts for pelbry hub and torvane miro and want to put it in their home.

Industry/Entity Type

Technology Equipment

Number of Pages Required

1 page

Colors

Designer to choose colors to be used in the design.

Requirements
Must have
• A great landing page, that is modern and attractive, that gets across the idea of smart devices and technology.
• Must be ios/android device friendly.
Nice to have
• interactive/animated buttons
• I like the direction and interactiveness of these websites, a simplified version would be awesome.
• Something in between:
• http://www.orbelfieldnest.com/ and https://plumtide.com/
• http://www.orbelfieldnest.com/

```html
<!DOCTYPE html>
<html lang="en">
<head>
<meta charset="utf-8">
<title>Corvo Halden – Smart Device Integration</title>
<link href="https://fonts.googleapis.com/css2?family=Nunito:wght@400;600;700&display=swap" rel="stylesheet">
<style>
:root{
  --blue:#5aa9e6;
  --blue-dark:#4a86b4;
  --nav-active:#4fa3dd;
  --ink:#3b3b3b;
  --ink-soft:#555;
  --panel:#ececec;
  --field:#ffffff;
  --white:#ffffff;
  --required:#d0262b;
  --brand-ink:#2d3440;
}
*{box-sizing:border-box;margin:0;padding:0}
html,body{width:1200px;height:2553px;overflow:hidden;background:var(--white)}
body{position:relative;font-family:'Nunito',Arial,sans-serif;color:var(--ink)}

.site-header{position:absolute;left:0;top:0;width:1200px;height:99px}
.brand{position:absolute;left:150px;top:24px;display:flex;align-items:center;gap:12px}
.brand-mark{width:52px;height:52px;border-radius:50%;background:var(--nav-active);flex:none}
.brand-name{font-size:30px;font-weight:700;color:var(--brand-ink);white-space:nowrap}
.main-nav{position:absolute;left:453px;top:31px;display:flex;gap:18px;font-size:24px;white-space:nowrap}
.main-nav a{color:var(--ink);text-decoration:none}
.main-nav a.is-active,.main-nav a.is-hover{color:var(--nav-active)}

.hero{position:absolute;left:0;top:99px;width:1200px;height:800px;
  background:linear-gradient(90deg,#d9dcdd 0%,#eef0f0 30%,#c9c4bc 55%,#4d4f52 72%,#3a3b3d 100%);
  color:var(--white);text-align:center;text-shadow:0 2px 5px rgba(0,0,0,.55)}
.hero-floor{position:absolute;left:0;bottom:0;width:100%;height:210px;
  background:linear-gradient(180deg,rgba(190,180,165,0),rgba(175,160,140,.55))}
.hero-title{position:absolute;top:158px;width:100%;font-size:66px;font-weight:700}
.hero-lead{position:absolute;top:445px;width:100%;font-size:32px;line-height:41px;font-weight:400}
.hero-sub{position:absolute;top:568px;width:100%;font-size:32px;font-weight:400}

.service{position:absolute;width:300px;height:352px;text-align:center}
.service-photo{display:block;width:150px;height:150px;border-radius:50%;margin:0 auto}
.service-title{margin-top:12px;font-size:18px;line-height:22px;font-weight:700;color:var(--ink)}
.service-text{margin-top:2px;font-size:17px;line-height:22.5px;color:var(--ink-soft)}
.btn{position:absolute;left:67px;top:313px;width:166px;height:38px;border-radius:3px;border:0;
  background:var(--blue);color:var(--white);font-family:'Nunito',Arial,sans-serif;font-size:18px;
  box-shadow:0 3px 4px rgba(0,0,0,.2)}
.btn.is-hover{background:var(--blue-dark)}

.panel{position:absolute;top:2068px;height:383px;width:442px;background:var(--panel);border-radius:6px}
.panel-title{text-align:center;font-size:30px;font-weight:600;color:var(--ink);margin-top:22px}
.testimonials{left:150px}
.quote{position:absolute;left:32px;top:84px;font-size:18px;color:var(--ink-soft)}
.quote-mark{font-size:40px;font-weight:700;color:#444;vertical-align:-12px;margin:0 4px}
.quote-author{position:absolute;right:44px;top:124px;font-size:14px;color:var(--ink-soft)}

.contact{left:608px}
.field{position:absolute;left:46px;width:350px;height:32px;background:var(--field);border:1px solid #d8d8d8;
  border-radius:4px;font-size:14px;color:#555;padding:6px 14px}
.field .req{color:var(--required)}
.checkbox-row{position:absolute;left:54px;top:171px;font-size:13px;color:#555;display:flex;align-items:center;gap:8px}
.checkbox{width:13px;height:13px;border:1px solid #555;background:var(--white)}
.submit{position:absolute;left:267px;top:296px;width:129px;height:28px;border:0;border-radius:4px;
  background:var(--blue);color:var(--white);font-family:'Nunito',Arial,sans-serif;font-size:14px;font-weight:700}
.contact-note{position:absolute;left:0;top:338px;width:100%;text-align:center;font-size:13px;line-height:18px;color:#555}

.site-footer{position:absolute;left:150px;top:2481px;width:900px;height:36px}
.copyright{position:absolute;left:0;top:7px;font-size:15px;color:var(--ink-soft)}
.copyright a{color:var(--nav-active);margin-left:14px}
.social{position:absolute;right:0;top:0;display:flex;gap:6px}
.social a{width:34px;height:34px;border-radius:50%;background:var(--blue);color:var(--white);
  text-decoration:none;font-size:15px;font-weight:700;display:flex;align-items:center;justify-content:center}
</style>
</head>
<body>

<header class="site-header">
  <div class="brand"><span class="brand-mark"></span><span class="brand-name">Corvo Halden</span></div>
  <nav class="main-nav">
    <a href="#" class="is-active">Home</a>
    <a href="#">What We Do</a>
    <a href="#">Products</a>
    <a href="#">About Us</a>
    <a href="#" class="is-hover">Contact Us</a>
  </nav>
</header>

<section class="hero" role="img" aria-label="Bright modern living room with tall white windows, leather armchairs, a round side table and hanging bulb lights against a dark wall">
  <div class="hero-floor"></div>
  <h1 class="hero-title">Smart Device Integration</h1>
  <p class="hero-lead">We are focused on delivering affordable and easily usable<br>devices for your home and office</p>
  <p class="hero-sub">Wireless Smart home – no need for pre-wired cabling</p>
</section>

<article class="service" style="left:129px;top:929px">
  <span class="service-photo" role="img" aria-label="Glowing light bulb illustration" style="background:radial-gradient(circle at 45% 45%,#f2b33a,#e7e4dc 70%)"></span>
  <h3 class="service-title">Home Automation</h3>
  <p class="service-text">Show us your Vision and we'll<br>create reality, by bringing<br>technology and your home or<br>office together.</p>
  <button class="btn">Read More</button>
</article>
<article class="service" style="left:451px;top:929px">
  <span class="service-photo" role="img" aria-label="Voice assistant speaker with floating smart home icons" style="background:radial-gradient(circle at 50% 70%,#3a8fd8,#6a4a34 60%,#9a6b45)"></span>
  <h3 class="service-title">Voice Control With Torvane Miro</h3>
  <p class="service-text">Your own concierge in a box,<br>control your home devices,<br>lights and music with voice<br>commands.</p>
  <button class="btn">Read More</button>
</article>
<article class="service" style="left:771px;top:929px">
  <span class="service-photo" role="img" aria-label="Hand holding a phone beside a keyless door lock" style="background:radial-gradient(circle at 40% 50%,#5a4a40,#1c1b1b 70%)"></span>
  <h3 class="service-title">Keyless Entry</h3>
  <p class="service-text">With myriad keyless options,<br>from thumbprint to touchless, it<br>makes unlocking your door and<br>giving access to guests a secure<br>and pleasant experience.</p>
  <button class="btn">Read More</button>
</article>

<article class="service" style="left:129px;top:1307px">
  <span class="service-photo" role="img" aria-label="Home cinema room with a large lit screen" style="background:radial-gradient(circle at 55% 50%,#b04a6a,#141822 65%)"></span>
  <h3 class="service-title">Home Theatre Design</h3>
  <p class="service-text">Home cinema's designed and<br>fitted to meet the specifications<br>of your unique home. Creating a<br>cinematic experience at any<br>budget.</p>
  <button class="btn">Read More</button>
</article>
<article class="service" style="left:451px;top:1307px">
  <span class="service-photo" role="img" aria-label="Bedroom window with automated blinds" style="background:linear-gradient(180deg,#c9cfd3,#8e8880 70%,#5a554f)"></span>
  <h3 class="service-title">Blind and Curtain Automation</h3>
  <p class="service-text">Automate any blind or curtain<br>in minutes, controllable<br>through an app or schedule<br>times and weather conditions.</p>
  <button class="btn is-hover">Read More</button>
</article>
<article class="service" style="left:771px;top:1307px">
  <span class="service-photo" role="img" aria-label="Phone showing a video doorbell feed beside a doorbell unit" style="background:linear-gradient(90deg,#c9ccc9,#e6e3dd 60%,#b8b2a6)"></span>
  <h3 class="service-title">Video Doorbell and Intercom</h3>
  <p class="service-text">Fit a video doorbell and intercom<br>post build, with options to suit<br>any home size or type.</p>
  <button class="btn">Read More</button>
</article>

<article class="service" style="left:129px;top:1686px">
  <span class="service-photo" role="img" aria-label="Modern house with an open garage at dusk" style="background:linear-gradient(180deg,#7f8b96,#c8a27a 55%,#5b5550)"></span>
  <h3 class="service-title">Smart Garage Doors</h3>
  <p class="service-text">Automatic garage door opening<br>as you drive up. Notifying you<br>when your garage door is opened<br>and allowing you to open it wher-<br>ever you are in the world.</p>
  <button class="btn">Read More</button>
</article>
<article class="service" style="left:451px;top:1686px">
  <span class="service-photo" role="img" aria-label="Television wall of streaming media tiles" style="background:radial-gradient(circle at 50% 45%,#3f8fc9,#0f2a44 70%)"></span>
  <h3 class="service-title">Media Entertainment</h3>
  <p class="service-text">Streamvale or your own personal<br>video collection on any TV or<br>multiple TV's throughout the<br>home.</p>
  <button class="btn">Read More</button>
</article>
<article class="service" style="left:771px;top:1686px">
  <span class="service-photo" role="img" aria-label="Overhead floor plan of a home with speakers in each room" style="background:radial-gradient(circle,#c9c6bf,#8f8a82 75%)"></span>
  <h3 class="service-title">Multiroom Audio</h3>
  <p class="service-text">Audio throughout the home,<br>have your music follow you<br>wherever you are, controllable<br>by phone or computer.</p>
  <button class="btn">Read More</button>
</article>

<section class="panel testimonials">
  <h2 class="panel-title">Client testimonials</h2>
  <p class="quote"><span class="quote-mark">“</span>Incredible value and peace of mind.<span class="quote-mark">”</span></p>
  <p class="quote-author">Maren T. Hollis, Athens, GA</p>
</section>

<section class="panel contact">
  <h2 class="panel-title">Contact Us</h2>
  <div class="field" style="top:78px">Name <span class="req">*</span></div>
  <div class="field" style="top:126px">E-mail <span class="req">*</span></div>
  <div class="checkbox-row"><span class="checkbox"></span>I want to receive e-mail updates</div>
  <div class="field" style="top:199px">Message <span class="req">*</span></div>
  <div class="field" style="top:247px">Comments</div>
  <button class="submit">Submit</button>
  <p class="contact-note">If you're not an auto form person, we understand.<br>Contact us at: info@corvohalden.com.au</p>
</section>

<footer class="site-footer">
  <p class="copyright">Copyright © 2017 Corvo Halden - All Rights Reserved.<a href="#">PRIVACY POLICY.</a></p>
  <nav class="social">
    <a href="#" aria-label="Flitter">F</a>
    <a href="#" aria-label="Circlo">C</a>
    <a href="#" aria-label="Chatterloop">C</a>
    <a href="#" aria-label="Snapquill">S</a>
  </nav>
</footer>

</body>
</html>
```